Lucky Orbit Fun Casino Entertainment

Looking to update my business card and make it look more modern, stand out and eye catching.
We are are fun casino business in Australia (primarily Sydney). Blackjack and Roulette are our most popular games although we have pretty much every game available for hire that you would find in a real casino. The final design would need to be sleek and appeal to the more upmarket corporate sector.
We mainly cater for Corporate Events, Private Parties, Fundraising Events, Team Building, Poker Tournaments
I think I'd prefer the colour Black.

Target Market(s)

High-end Corporate

Industry/Entity Type

Events

Contact Information for Business Card

Dale Hutchins
Director
1300 482 617
0431 758 209
info@luckyorbit.com.au
www.luckyorbit.com.au
Facebook & Instagram @luckyorbitshows (proper social icons preferred)

Colors
000000
0255a3

Requirements
Must have
• Front side:
• Logo
• Contact details
• 'Australia's #1 Fun Casino Specialists'
• Back:
• Logo
Nice to have
• Back:
• Corporate Events
• Private Parties
• Poker Tournaments
• Fundraising
• Props & Theming
• Photo Booth
• Horse Racing Events
• The Vegas Sign attached, maybe on the back of the card in the background...?

```html
<!DOCTYPE html>
<html lang="en">
<head>
<meta charset="utf-8">
<title>Lucky Orbit – Business Cards</title>
<link href="https://fonts.googleapis.com/css2?family=Titillium+Web:wght@300;400;600;700&display=swap" rel="stylesheet">
<style>
  :root {
    --stage: #2b2b2b;
    --card: #0b0b0b;
    --gold: #f5a51f;
    --white: #f2f2f2;
    --chip-dark: #2c2c2c;
    --chip-ring: #3a3a3a;
    --accent-blue: #0255a3;
  }
  * { box-sizing: border-box; margin: 0; padding: 0; }
  html, body { width: 1200px; height: 1021px; overflow: hidden; }
  body {
    background: var(--stage);
    font-family: "Titillium Web", sans-serif;
    position: relative;
  }
  .card {
    position: absolute;
    top: 200px;
    width: 380px;
    height: 620px;
    background: var(--card);
    overflow: hidden;
    box-shadow: 0 14px 36px rgba(0,0,0,.55);
  }
  .card--contact { left: 190px; }
  .card--services { left: 630px; }

  /* brand mark */
  .brand {
    display: flex;
    align-items: center;
    justify-content: center;
    gap: 14px;
  }
  .brand__dot {
    width: 46px; height: 46px;
    border-radius: 50%;
    background: var(--gold);
  }
  .brand__name {
    color: var(--gold);
    font-weight: 700;
    font-size: 40px;
    letter-spacing: 1px;
    line-height: 1;
  }

  /* contact side */
  .card--contact .brand { margin-top: 70px; }
  .person { text-align: center; margin-top: 70px; }
  .person__name { color: var(--gold); font-weight: 700; font-size: 30px; line-height: 1.1; }
  .person__role { color: var(--white); font-size: 17px; font-weight: 400; }
  .icons {
    display: flex; justify-content: center; gap: 8px; margin-top: 12px;
  }
  .icons svg { width: 22px; height: 22px; }
  .contacts {
    text-align: center; color: var(--white);
    font-size: 19px; font-weight: 300; line-height: 1.4; margin-top: 8px;
  }
  .rule {
    width: 260px; height: 1px; background: var(--gold); margin: 16px auto;
  }
  .social {
    display: flex; flex-direction: column; align-items: center; gap: 6px;
    color: var(--white); font-size: 19px; font-weight: 300;
  }
  .social__dot { width: 18px; height: 18px; border-radius: 50%; background: var(--gold); }
  .tagline {
    position: absolute; bottom: 30px; left: 0; right: 0; text-align: center;
    color: var(--gold); font-size: 21px; font-weight: 400;
  }
  .tagline__rank { color: var(--white); }

  /* services side */
  .sign-photo {
    position: absolute; top: 0; left: 0; right: 0; height: 350px;
    background:
      radial-gradient(ellipse at 45% 55%, #fff6cf 0%, #f7d36a 35%, #c9862a 65%, #3b1a08 100%);
  }
  .card--services .brand {
    position: absolute; top: 315px; left: 0; right: 0;
  }
  .services {
    position: absolute; top: 420px; left: 0; right: 0;
    text-align: center; color: var(--white);
    font-size: 19px; font-weight: 300; line-height: 1.55;
  }
  .services .sep { color: var(--gold); padding: 0 4px; }
</style>
</head>
<body>

<section class="card card--contact" aria-label="Business card, contact side">
  <div class="brand">
    <span class="brand__dot"></span>
    <span class="brand__name">Lucky Orbit</span>
  </div>

  <div class="person">
    <div class="person__name">Dale Hutchins</div>
    <div class="person__role">Director</div>
  </div>

  <div class="icons" aria-hidden="true">
    <svg viewBox="0 0 22 22"><circle cx="11" cy="11" r="11" fill="#f5a51f"/><path d="M7 6l2.5-.5 1.2 3-1.5 1a6 6 0 0 0 3.3 3.3l1-1.5 3 1.2L16 15c-5 .5-9.5-4-9-9z" fill="#0b0b0b"/></svg>
    <svg viewBox="0 0 22 22"><circle cx="11" cy="11" r="11" fill="#f5a51f"/><rect x="7.5" y="5" width="7" height="12" rx="1.2" fill="none" stroke="#0b0b0b" stroke-width="1.5"/></svg>
    <svg viewBox="0 0 22 22"><circle cx="11" cy="11" r="11" fill="#f5a51f"/><rect x="5.5" y="7" width="11" height="8" fill="none" stroke="#0b0b0b" stroke-width="1.4"/><path d="M5.5 7l5.5 4.5L16.5 7" fill="none" stroke="#0b0b0b" stroke-width="1.4"/></svg>
    <svg viewBox="0 0 22 22"><circle cx="11" cy="11" r="11" fill="#f5a51f"/><circle cx="11" cy="11" r="6" fill="none" stroke="#0b0b0b" stroke-width="1.3"/><ellipse cx="11" cy="11" rx="2.6" ry="6" fill="none" stroke="#0b0b0b" stroke-width="1.2"/><path d="M5 11h12" stroke="#0b0b0b" stroke-width="1.2"/></svg>
  </div>

  <div class="contacts">
    <div>1300 482 617</div>
    <div>0431 758 209</div>
    <div>info@luckyorbit.com.au</div>
    <div>www.luckyorbit.com.au</div>
  </div>

  <div class="rule"></div>

  <div class="social">
    <span class="social__dot" aria-hidden="true"></span>
    <span>@luckyorbitshows</span>
  </div>

  <p class="tagline">Australia's <span class="tagline__rank">#1</span> Fun Casino Specialists</p>
</section>

<section class="card card--services" aria-label="Business card, services side">
  <div class="sign-photo" role="img" aria-label="Photo of an illuminated welcome sign with bulb lights"></div>

  <div class="brand">
    <span class="brand__dot"></span>
    <span class="brand__name">Lucky Orbit</span>
  </div>

  <div class="services">
    <div>Corporate Events<span class="sep">|</span>Private Parties</div>
    <div>Poker Tournaments<span class="sep">|</span>Fundraising</div>
    <div>Props &amp; Theming<span class="sep">|</span>Photo Booth</div>
    <div>Horse Racing Events</div>
  </div>
</section>

</body>
</html>
```